Stonevale Business Card Design

The Stonevale Co is an aggregate (crushing) equipment dealer serving Western Canadian provinces. Stonevale is a distributor of aggregate equipment for different manufacturers.

We are looking to change and update the existing business card which has been used since the existence of the company. A copy of existing card has been attached for reference. The Stonevale Co logo we want to remain the same and we want the green color to remain the same.

We are wanting something new with a different look. A refreshing card to show a new modern and updated look. No longer wanting to have the manufacturers on the back of the card but something more like our logo on the back of the card with a statement like "Crushing Solutions"

ideas could be:
- card can be different colors on front and back
- front or reverse of the card could possibly be the green color with the logo in black

Target Market(s)

Owners of Aggregate/Crushing companies

Contact Information for Business Card

see above

Requirements
Must have
• - logo to remain same along with same font within logo
• - green color to remain same
Nice to have
• as noted above under project description
Should not have

```html
<!DOCTYPE html>
<html lang="en">
<head>
<meta charset="utf-8">
<title>The Stonevale Co — Business Card</title>
<link rel="stylesheet" href="https://fonts.googleapis.com/css2?family=Roboto:wght@400;500;700&family=Roboto+Condensed:wght@500&display=swap">
<style>
  :root {
    --brand-green: #878a0c;
    --brand-green-dark: #7c7f0a;
    --ink: #231f20;
    --ink-soft: #2b2a1c;
    --paper: #f4f4f4;
    --white: #ffffff;
    --backdrop: #e7e5e1;
  }
  * { margin: 0; padding: 0; box-sizing: border-box; }
  html, body { width: 1200px; height: 960px; overflow: hidden; }
  body {
    background: var(--backdrop);
    font-family: "Roboto", Arial, sans-serif;
    position: relative;
  }
  .card {
    position: absolute;
    left: 320px;
    width: 600px;
    height: 342px;
    border-radius: 20px;
    overflow: hidden;
  }
  /* Reverse side */
  .card--reverse {
    top: 108px;
    background: var(--brand-green);
  }
  .reverse-brand {
    position: absolute;
    right: 32px;
    top: 272px;
    text-align: right;
    color: var(--ink-soft);
  }
  .reverse-brand__name {
    font-weight: 700;
    font-size: 20px;
    letter-spacing: 0.2px;
  }
  .reverse-brand__tagline {
    font-weight: 500;
    font-size: 15px;
    margin-top: 5px;
    margin-right: 18px;
  }
  /* Front side */
  .card--front {
    top: 493px;
    background: var(--paper);
  }
  .card__wave {
    position: absolute;
    inset: 0;
    width: 600px;
    height: 342px;
  }
  .front-brand {
    position: absolute;
    left: 36px;
    top: 40px;
  }
  .front-brand__mark {
    display: block;
    width: 60px;
    height: 60px;
    border-radius: 50%;
    background: var(--brand-green);
    margin-left: 40px;
    margin-bottom: 50px;
  }
  .front-brand__name {
    font-weight: 700;
    font-size: 20px;
    color: var(--ink);
    letter-spacing: 0.2px;
  }
  .person {
    position: absolute;
    right: 24px;
    top: 148px;
    text-align: right;
  }
  .person__name {
    font-family: "Roboto Condensed", "Arial Narrow", sans-serif;
    font-weight: 500;
    font-size: 23px;
    color: var(--brand-green);
  }
  .person__title {
    font-size: 15px;
    color: var(--white);
    margin-top: 2px;
  }
  .contact-list {
    position: absolute;
    right: 26px;
    top: 204px;
    list-style: none;
    text-align: right;
  }
  .contact-list li {
    display: flex;
    align-items: center;
    justify-content: flex-end;
    gap: 9px;
    font-size: 14.5px;
    line-height: 19.5px;
    color: var(--white);
  }
  .contact-list svg { width: 12px; height: 12px; fill: var(--brand-green); }
  .address {
    position: absolute;
    right: 24px;
    top: 304px;
    font-size: 14.5px;
    color: var(--white);
  }
</style>
</head>
<body>

<section class="card card--reverse">
  <div class="reverse-brand">
    <div class="reverse-brand__name">THE STONEVALE CO.</div>
    <div class="reverse-brand__tagline">Crushing Solutions</div>
  </div>
</section>

<section class="card card--front">
  <svg class="card__wave" viewBox="0 0 600 342" aria-hidden="true">
    <path d="M0,268 C120,328 240,332 335,222 C425,118 500,78 600,72 L600,342 L0,342 Z" fill="var(--ink)"/>
    <path d="M0,284 C120,334 250,330 350,232 C440,140 510,100 600,92" fill="none" stroke="var(--white)" stroke-width="7"/>
  </svg>

  <div class="front-brand">
    <span class="front-brand__mark"></span>
    <div class="front-brand__name">THE STONEVALE CO.</div>
  </div>

  <div class="person">
    <div class="person__name">DALE MORROW</div>
    <div class="person__title">CEO/FOUNDER</div>
  </div>

  <ul class="contact-list">
    <li>780.555.0142
      <svg viewBox="0 0 12 12"><path d="M2.5 0.5l2 2.3-1 1.2c.7 1.6 1.9 2.8 3.5 3.5l1.2-1 2.3 2-1.3 2.3C4.6 10.4 1.6 7.4 0.2 1.8z"/></svg>
    </li>
    <li>780.555.0187
      <svg viewBox="0 0 12 12"><path d="M3 0h6v12H3z M4 1v8.5h4V1z M5.4 10.2h1.2v1h-1.2z" fill-rule="evenodd"/></svg>
    </li>
    <li>780.555.0163
      <svg viewBox="0 0 12 12"><path d="M3 1h6v3H3z M0.5 4.5h11v5H9.5v2h-7v-2H0.5z M3.5 8v2.5h5V8z" fill-rule="evenodd"/></svg>
    </li>
    <li>dale@stonevl.com
      <svg viewBox="0 0 12 12"><path d="M0.5 2.5h11v1L6 7 0.5 3.5z M0.5 4.8L6 8.3l5.5-3.5v4.7h-11z"/></svg>
    </li>
    <li>www.stonevale.ca
      <svg viewBox="0 0 12 12"><circle cx="6" cy="6" r="5.5"/></svg>
    </li>
  </ul>

  <div class="address">2215- 48B Avenue, Ridgeford, Alberta T4X 2M8</div>
</section>

</body>
</html>
```